Wired Earphone Creative Packaging Design

We would like a creative window box style packaging design for our wired earphone

Size: 6” x 3.5” x 1.5” (enclosed die-cut drawing)
Material: E Flute Paper box
Type: Window Box style
Design features we prefer: friendly, playful, creative, trendy, unique, High tech.
Competitors: Enclosed
Requirement:AI file is preferred

Enclosed are product pictures, marketing materials and competitor designs for your reference.

Any further questions, please feel free to ask.
Updates

So designers get more time to design

Target Market(s)

13-40 Year Olds

Industry/Entity Type

Audio

Colors

Designer to choose colors to be used in the design.

Requirements
Must have
• Window, selling point, creative

```html
<!DOCTYPE html>
<html lang="en">
<head>
<meta charset="utf-8">
<title>Customizable Stereo In-Ear Earbuds – Window Box Dieline</title>
<link href="https://fonts.googleapis.com/css2?family=Montserrat:wght@600;700;800&family=Bebas+Neue&family=Audiowide&display=swap" rel="stylesheet">
<style>
  :root {
    --bg: #ffffff;
    --cyan: #00ffff;
    --aqua: #33d6f5;
    --blue: #1aa3ef;
    --ink: #2b2b2b;
    --window: #333333;
    --dieline: #33ff33;
    --dim: #22ee22;
    --white: #ffffff;
  }
  html, body { margin: 0; padding: 0; overflow: hidden; background: var(--bg); }
  .artboard { display: block; width: 1200px; height: 900px; }
  .headline { font-family: "Montserrat", sans-serif; font-weight: 800; fill: var(--ink); }
  .tag-box { fill: var(--white); stroke: var(--aqua); stroke-width: 1.2; }
  .tag-text { font-family: "Bebas Neue", sans-serif; fill: var(--aqua); text-anchor: middle; }
  .info { font-family: "Bebas Neue", sans-serif; fill: var(--ink); text-anchor: middle; }
  .info-head { font-family: "Bebas Neue", sans-serif; fill: var(--white); text-anchor: middle; }
  .model-small { font-family: "Montserrat", sans-serif; font-weight: 700; fill: var(--white); text-anchor: middle; }
  .model-code { font-family: "Audiowide", sans-serif; fill: var(--white); text-anchor: middle; }
  .feature-label { font-family: "Bebas Neue", sans-serif; fill: var(--white); text-anchor: middle; font-size: 6.5px; letter-spacing: 0.4px; }
  .cut { fill: none; stroke: var(--dieline); stroke-width: 0.9; }
  .fold { fill: none; stroke: var(--dieline); stroke-width: 0.9; stroke-dasharray: 3 2; }
  .dim-line { stroke: var(--dim); stroke-width: 0.9; fill: none; }
  .dim-text { font-family: "Montserrat", sans-serif; font-weight: 700; font-size: 12px; fill: var(--dim); }
</style>
</head>
<body>
<svg class="artboard" viewBox="0 0 1084 815" preserveAspectRatio="none" xmlns="http://www.w3.org/2000/svg">
  <defs>
    <linearGradient id="mosaic-tone" x1="0" y1="0" x2="1" y2="1">
      <stop offset="0" stop-color="#5fe6fb"/>
      <stop offset="0.5" stop-color="#2ab8f2"/>
      <stop offset="1" stop-color="#44d0f8"/>
    </linearGradient>
  </defs>

  <g class="dimensions">
    <line class="dim-line" x1="233" y1="5" x2="233" y2="729"/>
    <line class="dim-line" x1="226" y1="5" x2="300" y2="5"/>
    <line class="dim-line" x1="226" y1="729" x2="560" y2="729"/>
    <text class="dim-text" transform="translate(238 388) rotate(-90)">256.00</text>
    <line class="dim-line" x1="303" y1="803" x2="1080" y2="803"/>
    <line class="dim-line" x1="303" y1="585" x2="303" y2="810"/>
    <line class="dim-line" x1="1080" y1="575" x2="1080" y2="810"/>
    <rect x="666" y="796" width="44" height="14" fill="var(--bg)"/>
    <text class="dim-text" x="668" y="808">274.00</text>
  </g>

  <polygon class="mosaic" role="img" aria-label="Blue pixel mosaic pattern" fill="url(#mosaic-tone)"
    points="290,155 740,155 740,226 528,256 528,528 290,550"/>
  <polygon class="mosaic" role="img" aria-label="Blue pixel mosaic pattern" fill="url(#mosaic-tone)"
    points="663,520 915,500 915,578 663,578"/>

  <polygon class="back-panel" fill="var(--cyan)" points="290,48 555,48 555,155 490,155 490,508 290,537"/>
  <rect class="hang-hole" x="357" y="96" width="145" height="12" rx="6" fill="none" stroke="var(--dieline)" stroke-width="0.9"/>
  <rect class="hang-slot" x="347" y="153" width="165" height="8" fill="none" stroke="var(--dieline)" stroke-width="0.9"/>
  <path class="cut" d="M306 52 V155 M306 52 H553"/>

  <g class="back-copy">
    <text class="headline" x="320" y="200" font-size="16" textLength="154" lengthAdjust="spacingAndGlyphs">CUSTOMIZABLE</text>
    <rect class="tag-box" x="320" y="206" width="62" height="12"/>
    <text class="tag-text" x="351" y="216" font-size="10.5" textLength="56" lengthAdjust="spacingAndGlyphs">STEREO IN-EAR</text>
    <text class="headline" x="385" y="217" font-size="15" textLength="89" lengthAdjust="spacingAndGlyphs">EARBUDS</text>

    <text class="info-head" x="390" y="270" font-size="13">CONTENTS:</text>
    <text class="info" x="390" y="290" font-size="11">2 PAIRS OF SWITCHABLE CAPS</text>
    <text class="info" x="390" y="311" font-size="11">3 PAIRS OF SILICON EAR TIPS</text>
    <text class="info" x="390" y="332" font-size="11">USER MANUAL</text>

    <text class="info-head" x="390" y="381" font-size="13">SPECIFICATIONS:</text>
    <text class="info" x="390" y="401" font-size="11">FREQUENCY RESPONSE: 20-20KHz</text>
    <text class="info" x="390" y="422" font-size="11">SENSITIVITY: 105 3dB</text>
    <text class="info" x="390" y="443" font-size="11">THD: &lt;3%</text>
    <text class="info" x="390" y="465" font-size="11">CORD LENGTH: 3.6ft</text>
  </g>

  <g class="model-badge">
    <text class="model-small" x="612" y="176" font-size="4.5">MODEL NO.</text>
    <text class="model-code" x="612" y="195" font-size="21">KX-7</text>
    <text class="model-small" x="612" y="209" font-size="6" font-weight="600">INCLUDES</text>
    <text class="model-small" x="612" y="216" font-size="6">MULTI-FUNCTION</text>
    <text class="model-small" x="612" y="223" font-size="6" font-weight="600">CONTROLLER</text>
  </g>
  <g class="model-badge">
    <text class="model-small" x="700" y="176" font-size="4.5">MODEL NO.</text>
    <text class="model-code" x="703" y="195" font-size="21">KX-7</text>
    <text class="model-small" x="700" y="205" font-size="6" font-weight="600">INCLUDES</text>
    <text class="model-small" x="700" y="212" font-size="6">MULTI-FUNCTION</text>
    <text class="model-small" x="700" y="220" font-size="6" font-weight="600">CONTROLLER</text>
  </g>

  <g class="front-headline">
    <text class="headline" x="750" y="185" font-size="16" textLength="152" lengthAdjust="spacingAndGlyphs">CUSTOMIZABLE</text>
    <rect class="tag-box" x="750" y="190" width="62" height="12"/>
    <text class="tag-text" x="781" y="200" font-size="10.5" textLength="56" lengthAdjust="spacingAndGlyphs">STEREO IN-EAR</text>
    <text class="headline" x="815" y="201" font-size="15" textLength="88" lengthAdjust="spacingAndGlyphs">EARBUDS</text>
  </g>

  <polygon class="window-accent" fill="var(--aqua)" points="638,238 943,207 945,497 640,518"/>
  <polygon class="window" fill="var(--window)" points="635,243 940,212 940,497 635,521"/>
  <polygon class="window-cut" fill="none" stroke="var(--dieline)" stroke-width="0.9" points="645,255 930,222 930,487 645,509"/>

  <g class="side-title" transform="translate(600 280) rotate(90)">
    <text class="headline" x="0" y="0" font-size="30" textLength="260" lengthAdjust="spacingAndGlyphs">CUSTOMIZABLE</text>
    <rect class="tag-box" x="0" y="9" width="103" height="19"/>
    <text class="tag-text" x="51.5" y="24" font-size="16" textLength="95" lengthAdjust="spacingAndGlyphs">STEREO IN-EAR</text>
    <text class="headline" x="110" y="29" font-size="30" textLength="150" lengthAdjust="spacingAndGlyphs">EARBUDS</text>
  </g>

  <g class="side-title" transform="translate(978 498) rotate(-90)">
    <text class="headline" x="0" y="0" font-size="30" textLength="258" lengthAdjust="spacingAndGlyphs">CUSTOMIZABLE</text>
    <rect class="tag-box" x="0" y="9" width="103" height="19"/>
    <text class="tag-text" x="51.5" y="24" font-size="16" textLength="95" lengthAdjust="spacingAndGlyphs">STEREO IN-EAR</text>
    <text class="headline" x="110" y="29" font-size="30" textLength="150" lengthAdjust="spacingAndGlyphs">EARBUDS</text>
  </g>

  <g class="features">
    <circle cx="700" cy="538" r="10" fill="var(--white)"/>
    <circle cx="743" cy="538" r="10" fill="var(--white)"/>
    <circle cx="790" cy="538" r="10" fill="var(--white)"/>
    <circle cx="835" cy="538" r="10" fill="var(--white)"/>
    <circle cx="880" cy="538" r="10" fill="var(--white)"/>
    <text class="feature-label" x="700" y="558">CUSTOMIZABLE</text>
    <text class="feature-label" x="700" y="566">EARBUD CAPS</text>
    <text class="feature-label" x="743" y="558">IN-LINE</text>
    <text class="feature-label" x="743" y="566">MIC</text>
    <text class="feature-label" x="790" y="558">SILICON GEL</text>
    <text class="feature-label" x="790" y="566">EARTIPS</text>
    <text class="feature-label" x="835" y="558">3.5mm</text>
    <text class="feature-label" x="835" y="566">JACK</text>
    <text class="feature-label" x="880" y="558">ERGONOMIC</text>
    <text class="feature-label" x="880" y="566">DESIGN</text>
  </g>

  <g class="dieline">
    <path class="fold" d="M303 155 H1020 M303 578 H1020 M555 155 V578 M663 155 V578 M915 155 V578 M1020 155 V578 M690 687 H890"/>
    <path class="cut" d="M303 155 V578"/>
    <path class="cut" d="M560 155 V70 Q560 55 575 55 H642 Q657 55 657 70 V155"/>
    <path class="cut" d="M600 60 V100 Q606 108 612 100 V60"/>
    <path class="cut" d="M665 155 V50 H705 V18 Q705 5 718 5 H862 Q875 5 875 18 V50 H915 V155"/>
    <path class="cut" d="M705 50 H875"/>
    <path class="cut" d="M920 155 V70 Q920 55 935 55 H1005 Q1020 55 1020 70 V155"/>
    <path class="cut" d="M962 60 V100 Q968 108 974 100 V60"/>
    <path class="cut" d="M1020 155 L1080 165 V570 L1020 578"/>
    <path class="cut" d="M560 578 V590 L570 675 H650 L657 590 V578"/>
    <path class="cut" d="M665 578 V687 H915 V578"/>
    <path class="cut" d="M668 687 V712 Q668 729 685 729 H895 Q912 729 912 712 V687"/>
    <path class="cut" d="M920 578 V590 L925 675 H1015 L1020 590 V578"/>
    <path class="cut" d="M303 578 V590 M1080 570 V578"/>
  </g>
</svg>
</body>
</html>
```